Thank you for shopping with us business card

We would like a thank you card for our rebranded business. We used to be "Brindle Goods" but are now "Marlow Finds. Old thank you card and new logo will be attached for reference. New thank you card does not have to be same design as old thank you card, but please use new logo.
Shopmart URL is now marlowfinds.shopmart.example
Instagram is @Marlow_Finds
Email is marlowfinds@mailbox.example
Thank you!

Contact Information for Business Card

Shopmart site, email, Instagram

```html
<!DOCTYPE html>
<html lang="en">
<head>
<meta charset="utf-8">
<title>Marlow Finds – Thank You Card</title>
<link href="https://fonts.googleapis.com/css2?family=Montserrat:wght@700&family=Pacifico&family=Outfit:wght@500&family=Nunito:wght@800&display=swap" rel="stylesheet">
<style>
  :root {
    --ink: #000000;
    --white: #ffffff;
    --sky-light: #a9dcea;
    --sky-top: #74a6d6;
    --teal: #1590bd;
    --navy: #0f4c6c;
    --azure: #3199d6;
    --ice: #a6dcea;
    --script-edge: #2c5470;
  }
  * { margin: 0; padding: 0; box-sizing: border-box; }
  html, body { width: 1052px; height: 1200px; overflow: hidden; }
  body { position: relative; background: var(--white); }

  .brand-panel {
    position: absolute; left: 0; top: 0; width: 1052px; height: 601px;
    background:
      radial-gradient(ellipse 420px 260px at 0 0, rgba(116,166,214,0.9), rgba(116,166,214,0) 100%),
      linear-gradient(90deg, var(--sky-light) 0%, var(--sky-light) 38%, #62b4d2 62%, #2b9ac3 80%, var(--teal) 100%);
  }
  .brand-mark {
    position: absolute; left: 446px; top: 170px;
    width: 160px; height: 160px;
    background: var(--ink);
  }
  .brand-name {
    position: absolute; left: 0; width: 100%; top: 408px;
    text-align: center;
    font-family: "Montserrat", sans-serif; font-weight: 700;
    font-size: 40px; line-height: 1; letter-spacing: 0.5px; color: var(--ink);
  }

  .thanks-panel {
    position: absolute; left: 0; top: 601px; width: 1052px; height: 599px;
    background:
      radial-gradient(ellipse 480px 340px at 1000px 620px, rgba(166,220,234,1) 0%, rgba(166,220,234,0.7) 35%, rgba(166,220,234,0) 75%),
      linear-gradient(90deg, var(--navy) 0%, var(--navy) 25%, #1d7bb0 50%, var(--azure) 65%, var(--azure) 100%);
  }
  .thanks-title {
    position: absolute; left: 0; width: 100%; top: 104px;
    text-align: center;
    font-family: "Pacifico", cursive; font-size: 128px; line-height: 1;
    color: var(--white);
    text-shadow: 3px 4px 0 var(--script-edge);
  }
  .thanks-sub {
    position: absolute; left: 0; width: 100%; top: 292px;
    text-align: center;
    font-family: "Outfit", sans-serif; font-weight: 500; font-size: 54px;
    line-height: 1; color: var(--white);
  }

  .contact-list { position: absolute; left: 64px; top: 397px; list-style: none; }
  .contact-item { display: flex; align-items: center; height: 51px; }
  .contact-icon { width: 50px; height: 40px; flex: none; }
  .contact-text {
    margin-left: 16px;
    font-family: "Nunito", sans-serif; font-weight: 800; font-size: 24px;
    letter-spacing: 0.8px; color: var(--white);
  }
</style>
</head>
<body>
  <section class="brand-panel">
    <div class="brand-mark" aria-hidden="true"></div>
    <h1 class="brand-name">MARLOW FINDS</h1>
  </section>

  <section class="thanks-panel">
    <h2 class="thanks-title">Thank You</h2>
    <p class="thanks-sub">For Shopping With Us</p>

    <ul class="contact-list">
      <li class="contact-item">
        <svg class="contact-icon" viewBox="0 0 50 40" aria-hidden="true">
          <rect x="4" y="2" width="42" height="26" rx="4" fill="none" stroke="#fff" stroke-width="3"/>
          <line x1="25" y1="28" x2="25" y2="36" stroke="#fff" stroke-width="3"/>
          <line x1="16" y1="37" x2="34" y2="37" stroke="#fff" stroke-width="3"/>
        </svg>
        <span class="contact-text">marlowfinds.shopmart.example</span>
      </li>
      <li class="contact-item">
        <svg class="contact-icon" viewBox="0 0 50 40" aria-hidden="true">
          <rect x="8" y="2" width="36" height="36" fill="none" stroke="#fff" stroke-width="3"/>
        </svg>
        <span class="contact-text">@Marlow_Finds</span>
      </li>
      <li class="contact-item">
        <svg class="contact-icon" viewBox="0 0 50 40" aria-hidden="true">
          <rect x="2" y="4" width="46" height="32" rx="4" fill="none" stroke="#fff" stroke-width="3"/>
          <polyline points="4,7 25,23 46,7" fill="none" stroke="#fff" stroke-width="3" stroke-linejoin="round"/>
        </svg>
        <span class="contact-text">marlowfinds@mailbox.example</span>
      </li>
    </ul>
  </section>
</body>
</html>
```